ORVALO Global Commerce Inc.
Kareem Bin-Sahwan
Vice President
Unit 385, 2096 Pellmore Crescent Toronto, Ontario, Canada M4R 2K6
kareem@orvaloglobal.ca
www.orvaloglobal.ca
The company's name is "ORVALO Global Commerce Inc." The company's new logo is only stating ORVALO, i need the wording "Global Commerce Inc." to be added next to the logo at different designs for me to choose from.
The logo of the company with the wording "Global Commerce Inc." at different backgrounds and design for me to choose from.

```html
<!DOCTYPE html>
<html lang="en">
<head>
<meta charset="utf-8">
<title>ORVALO Global Commerce Inc. – Business Card</title>
<link rel="stylesheet" href="https://fonts.googleapis.com/css2?family=Oswald:wght@300;400;500&family=Open+Sans:wght@400;600&display=swap">
<style>
  :root {
    --backdrop: #d9dadc;
    --card: #ffffff;
    --brand-blue: #2a8fd0;
    --ink: #3b3f45;
    --ink-soft: #6a6f76;
    --divider: #2f3338;
    --shadow: rgba(0,0,0,0.18);
  }
  * { box-sizing: border-box; margin: 0; padding: 0; }
  html, body { width: 1200px; height: 946px; overflow: hidden; }
  body {
    background: var(--backdrop);
    font-family: "Open Sans", Arial, sans-serif;
    color: var(--ink);
    position: relative;
  }
  .card {
    position: absolute;
    top: 123px;
    width: 400px;
    height: 700px;
    background: var(--card);
    border-radius: 22px;
    box-shadow: 0 14px 34px var(--shadow);
  }
  .card--back { left: 150px; }
  .card--front { left: 650px; padding: 66px 48px 0 48px; }

  /* front: brand lockup */
  .brand {
    display: flex;
    align-items: flex-start;
    gap: 16px;
  }
  .brand__mark {
    width: 22px;
    height: 62px;
    margin-top: 2px;
    background: var(--brand-blue);
    flex: none;
  }
  .brand__text { display: flex; flex-direction: column; }
  .brand__name {
    font-family: "Oswald", Arial, sans-serif;
    font-weight: 300;
    font-size: 64px;
    line-height: 1;
    letter-spacing: 4px;
    color: var(--ink);
  }
  .brand__tagline {
    font-family: "Oswald", Arial, sans-serif;
    font-weight: 400;
    font-size: 15px;
    line-height: 1;
    letter-spacing: 3.2px;
    text-transform: uppercase;
    color: var(--brand-blue);
    margin-top: 10px;
  }

  .person { margin-top: 36px; padding-left: 38px; }
  .person__name {
    font-family: "Oswald", Arial, sans-serif;
    font-weight: 400;
    font-size: 26px;
    letter-spacing: 1.5px;
    text-transform: uppercase;
    color: var(--brand-blue);
  }
  .person__title {
    font-size: 14px;
    color: var(--ink-soft);
    margin-top: 2px;
  }
  .contacts { margin-top: 54px; list-style: none; }
  .contact {
    display: flex;
    align-items: center;
    margin-bottom: 44px;
  }
  .contact__icon { width: 34px; height: 34px; flex: none; }
  .contact__rule {
    width: 3px;
    height: 44px;
    background: var(--divider);
    margin: 0 16px 0 18px;
    flex: none;
  }
  .contact__lines { font-size: 14px; line-height: 1.55; color: var(--ink); }

  /* back */
  .socials {
    position: absolute;
    right: 28px;
    bottom: 30px;
    display: flex;
    gap: 18px;
  }
  .social {
    display: flex;
    align-items: center;
    gap: 6px;
    font-size: 11px;
    color: var(--ink-soft);
  }
  .social__box { width: 14px; height: 14px; background: var(--brand-blue); }
</style>
</head>
<body>
  <section class="card card--back" aria-label="Card back">
    <div class="socials">
      <span class="social"><span class="social__box"></span>/kbsahwan</span>
      <span class="social"><span class="social__box"></span>/kbsahwan</span>
    </div>
  </section>

  <section class="card card--front" aria-label="Card front">
    <div class="brand">
      <span class="brand__mark"></span>
      <div class="brand__text">
        <span class="brand__name">ORVALO</span>
        <span class="brand__tagline">Global Commerce Inc.</span>
      </div>
    </div>

    <div class="person">
      <p class="person__name">Kareem Bin-Sahwan</p>
      <p class="person__title">Vice President</p>
    </div>

    <ul class="contacts">
      <li class="contact">
        <svg class="contact__icon" viewBox="0 0 34 34" aria-hidden="true">
          <circle cx="17" cy="10" r="7" fill="var(--brand-blue)"/>
          <path d="M3 32 C3 22 9 19 17 19 C25 19 31 22 31 32 Z" fill="var(--brand-blue)"/>
        </svg>
        <span class="contact__rule"></span>
        <p class="contact__lines">+1 416 555 0187<br>+1 647 555 0142</p>
      </li>
      <li class="contact">
        <svg class="contact__icon" viewBox="0 0 34 34" aria-hidden="true">
          <path d="M17 2 C10 2 6 7 6 13 C6 21 17 32 17 32 C17 32 28 21 28 13 C28 7 24 2 17 2 Z" fill="var(--brand-blue)"/>
          <circle cx="17" cy="13" r="4.5" fill="var(--card)"/>
        </svg>
        <span class="contact__rule"></span>
        <p class="contact__lines">Unit 385, 2096 Pellmore Crescent<br>Toronto, Ontario, Canada M4R 2K6</p>
      </li>
      <li class="contact">
        <svg class="contact__icon" viewBox="0 0 34 34" aria-hidden="true">
          <g fill="none" stroke="var(--brand-blue)" stroke-width="2.4">
            <circle cx="17" cy="17" r="14"/>
            <ellipse cx="17" cy="17" rx="6" ry="14"/>
            <line x1="3" y1="17" x2="31" y2="17"/>
            <line x1="6" y1="10" x2="28" y2="10"/>
            <line x1="6" y1="24" x2="28" y2="24"/>
          </g>
        </svg>
        <span class="contact__rule"></span>
        <p class="contact__lines">kareem@orvaloglobal.ca<br>www.orvaloglobal.ca</p>
      </li>
    </ul>
  </section>
</body>
</html>
```